Wine label - premium, elegant & classic

We are a young husband and wife team who have worked in the wine industry for 10+ years. This year we've finally had the opportunity to make our own wine and release our own brand. Our wines are boutique and sell at a mid-premium price (we don't make a lot) so we're looking for a label design that can reflect this premium nature and mixes traditional design elements with modern reflections.

The brand is called: M&L
Updates

Project Deadline Extended
Reason: We've received some great design concepts over the past week which we would happily pay for, so we've decided to guarantee payment and extend the deadline to allow time for more designs to be sent through. A BIG thanks to all who have already submitted, your designs are still under consideration. Cheers, L.

A big thank you to all for taking the time to submit your beautiful designs to our project.  We now have the very tough job of looking over each of them and selecting only one.  We hope to come to a decision in the next day or two, so hopefully we won't keep you waiting too long!

Cheers, and thanks again

M&L.                                   

Target Market(s)

30 - 45 year old female and male wine drinkers

Industry/Entity Type

Industry

Requirements
Must have
• Can we please see two versions of the one design - one for a red wine and one for a white wine.

The front labels needs to include the following information:
1. Brand name: M&L
2. Wine varieties: Pinot Noir (red wine) and Sauvignon Blanc (white wine)
3. Vintage: 2012 for both
4. Region: Yarra Valley
5. GI: Wine of Australia (not essential to be on front label)

The back label needs to include the following:
1. The brand name: M&L
2. Variety, vintage, region and volume (the volume must be 4mm in height)
3. Room for product description - approx. 30-40 words.
4. Alcohol statement (no size restriction, pls use 12.5% ALC/VOL as example)
5. Standard drinks (no size restriction, pls use 'Approx.7.8 standard drinks' as example)
6. Sulphites statement: "Sulphites added."
7. Allergen statement: "Fined with the aid of egg and milk products and traces may remain."
8. Room for address: Approx. 20 words
9. "Wine of Australia" - no size restriction, just needs to be legible

Packaging presentation:
Pinot Noir is a red wine and Sauvignon Blanc is a white wine.
Labels for both need to be shown on premium punted burgundy bottles (pls see example: http://www.pelvornglass.com/products_services/pvg_premium_burgundy_750_ml_wine_bottle.html)
Nice to have
• We would like the design to embody the following elements:
1. Classically modern
2. Clean and simple
3. Elegance
4. Restricted use of colours (ideally just black/grey, white/buff and perhaps one other)

Some design examples of what we like:
1. http://www.fenwickhollow.com.au/sangiovese-tasting-notes/
2. http://corlunbend.com/Wines/Corlun-Bend-Vineyard/Range/2010-Corlun-Bend-Single-Vineyard-Pinot-Noir-.htm
Should not have
• Preferrably won't have any photos or drawings unless you feel there is a simple symbol or image that could be used to enhance the design.

Restricted use of colours - more muted, conservative tones.

```html
<!DOCTYPE html>
<html lang="en">
<head>
<meta charset="utf-8">
<title>M&amp;L Wine label design: option 1</title>
<link rel="stylesheet" href="https://fonts.googleapis.com/css2?family=Cinzel:wght@400&family=Source+Sans+3:wght@400;600;700&family=Arimo:wght@400&display=swap">
<style>
  :root {
    --page: #ffffff;
    --ink: #1a1a1a;
    --cream: #fdf6e7;
    --taupe: #c4b7af;
    --stone: #d6cfca;
    --mono-grey: #b5aca7;
    --label-text: #5b4f49;
    --rule: #cfc6c0;
    --frame: #d9d4d0;
    --white: #ffffff;
  }
  * { box-sizing: border-box; margin: 0; padding: 0; }
  html, body { width: 1200px; height: 848px; overflow: hidden; }
  body { background: var(--page); font-family: "Source Sans 3", Arial, sans-serif; color: var(--ink); position: relative; }

  .brief-note { position: absolute; left: 568px; top: 64px; width: 560px; font-size: 15px; line-height: 19px; }
  .brief-note h1 { font-size: 14.5px; font-weight: 700; }

  .label { position: absolute; text-align: center; font-family: "Cinzel", serif; color: var(--label-text); }
  .label .brand { display: block; font-family: "Cinzel", serif; font-weight: 400; line-height: 1; }
  .label .variety { letter-spacing: 0.08em; }
  .label .vintage { display: inline-block; border-top: 1px solid var(--rule); letter-spacing: 0.05em; }

  /* flat front labels (shelf pair) */
  .front-mini { top: 473px; height: 206px; }
  .front-mini.red { left: 100px; width: 143px; background: var(--stone); color: var(--white); }
  .front-mini.white { left: 311px; width: 157px; background: var(--cream); }
  .front-mini .brand { margin-top: 42px; font-size: 30px; }
  .front-mini.red .brand { color: var(--white); }
  .front-mini.white .brand { color: var(--mono-grey); }
  .front-mini .variety { margin-top: 18px; font-size: 7px; }
  .front-mini .vintage { margin-top: 1px; font-size: 7px; padding-top: 1px; }
  .front-mini .region { position: absolute; left: 0; right: 0; bottom: 22px; font-size: 5.5px; letter-spacing: 0.05em; }

  /* front label artwork */
  .front { left: 562px; top: 229px; width: 255px; height: 363px; background: var(--cream); border: 1px solid var(--frame); }
  .front .brand { margin-top: 78px; font-size: 64px; color: var(--mono-grey); }
  .front .variety { margin-top: 26px; font-size: 12.5px; }
  .front .vintage { margin-top: 2px; width: 150px; padding-top: 2px; font-size: 12.5px; }
  .front .region { position: absolute; left: 0; right: 0; top: 322px; font-size: 9.5px; letter-spacing: 0.06em; }

  /* back label artwork */
  .back { left: 857px; top: 229px; width: 291px; height: 363px; background: var(--white); border: 1px solid var(--frame); }
  .back-top { height: 227px; background: var(--taupe); padding-top: 28px; }
  .back .brand { font-size: 34px; color: var(--white); }
  .back .variety { margin-top: 10px; font-size: 12.5px; }
  .back .vintage { margin-top: 1px; width: 150px; padding-top: 1px; font-size: 12.5px; }
  .back .description { font-family: "Arimo", Arial, sans-serif; font-size: 8.3px; line-height: 11.5px; color: var(--ink); margin: 9px 16px 0; }
  .back .description p + p { margin-top: 4px; }
  .back .address { margin-top: 9px; font-size: 8.6px; line-height: 10px; letter-spacing: 0.04em; }
  .back-bottom { position: relative; height: 134px; font-family: "Source Sans 3", Arial, sans-serif; text-align: left; color: var(--ink); }
  .abv { position: absolute; left: 17px; top: 20px; font-size: 13.5px; }
  .barcode-area { position: absolute; left: 17px; top: 40px; width: 125px; height: 78px; border: 1px solid var(--ink); font-family: "Arimo", Arial, sans-serif; font-size: 8.5px; display: flex; align-items: center; justify-content: center; }
  .sulphites { position: absolute; left: 148px; top: 6px; font-size: 10.5px; }
  .gi { position: absolute; left: 148px; top: 19px; font-size: 12.5px; }
  .allergen { position: absolute; left: 148px; top: 40px; width: 56px; font-size: 6.8px; line-height: 8px; }
  .volume { position: absolute; left: 146px; top: 95px; font-size: 19px; }
  .std-drinks { position: absolute; left: 222px; top: 46px; width: 55px; height: 76px; }
</style>
</head>
<body>

<section class="brief-note">
  <h1>M&amp;L Wine label design: option 1</h1>
  <p>Would suggest a raised varnish for the M&amp;L on both front and back,<br>with a matt paper with some kind of fine texture in it.</p>
</section>

<div class="label front-mini red">
  <span class="brand">M&amp;L</span>
  <div class="variety">Pinot Noir</div>
  <div class="vintage">2012</div>
  <div class="region">Yarra Valley, wine of australia</div>
</div>

<div class="label front-mini white">
  <span class="brand">M&amp;L</span>
  <div class="variety">Sauvignon Blanc</div>
  <div class="vintage">2012</div>
  <div class="region">Yarra Valley, wine of australia</div>
</div>

<div class="label front">
  <span class="brand">M&amp;L</span>
  <div class="variety">Sauvignon Blanc</div>
  <div class="vintage">2012</div>
  <div class="region">Yarra Valley, wine of australia</div>
</div>

<div class="label back">
  <div class="back-top">
    <span class="brand">M&amp;L</span>
    <div class="variety">Sauvignon Blanc</div>
    <div class="vintage">2012</div>
    <div class="description">
      <p>Rum eosande non natem fugitae nos cor se peruptature experfercium fuga. Es imenias rem re vendellorunt lam rerum et landa nem alitibus.</p>
      <p>At pelique sunt, sequund eritis serro volupta quamus molupta volorionesti omnimin ciliber ionsectaqui denimusdae doluptas dollia commolora simi, eosanti cus in esequuntem se vellorum.</p>
    </div>
    <div class="address">ADRESS DETAILS TO COME, ADRESS<br>DETAILS TO COME, YARRA VALLEY</div>
  </div>
  <div class="back-bottom">
    <div class="abv">12.5% Alc/Vol.</div>
    <div class="barcode-area">BARCODE AREA</div>
    <div class="sulphites">Contains Sulphites</div>
    <div class="gi">WINE OF AUSTRALIA</div>
    <div class="allergen">Fined with the aid of egg and milk products and traces may remain.</div>
    <div class="volume">750ml</div>
    <svg class="std-drinks" viewBox="0 0 55 76" role="img" aria-label="7.8 standard drinks">
      <text x="10" y="74" transform="rotate(-90 10 74)" font-family="Source Sans 3, Arial, sans-serif" font-weight="700" font-size="9.5" fill="#1a1a1a">Standard Drinks</text>
      <path d="M17 4 H51 L49 26 Q47 40 34 42 Q21 40 19 26 Z" fill="none" stroke="#1a1a1a" stroke-width="3"/>
      <path d="M19 10 H49 L48 26 Q46 38 34 39 Q22 38 20 26 Z" fill="#1a1a1a"/>
      <text x="34" y="28" text-anchor="middle" font-family="Source Sans 3, Arial, sans-serif" font-weight="700" font-size="14" fill="#ffffff">7.8</text>
      <rect x="32.5" y="42" width="3" height="20" fill="#1a1a1a"/>
      <rect x="22" y="61" width="24" height="3" fill="#1a1a1a"/>
    </svg>
  </div>
</div>

<div style="position:absolute;left:562px;top:609px;width:255px;text-align:center;font-size:12.5px;">Size: 70mm (w) x 100mm (h)</div>
<div style="position:absolute;left:857px;top:609px;width:291px;text-align:center;font-size:12.5px;">Size: 80mm (w) x 100mm (h)</div>

</body>
</html>
```